Market online tutoring + Back to School + give Support for students school work K to 12 Grade

To promote my tutoring business online need to create a two sided flyer. Need to get the attention of parents and educators who looking for help to support the digital learning of their students due to COVID-19 lock down. I need to project and differentiate that we offer support for online school with individualized learning . We tutor Elementary to High school students on all subjects you may take a look at my website qnacademyga.com for additional info and also I can provide
Updates

Hi All Due to Covid, we were unable to work on this project on time as originally planned. We were given an extension until March 15 and we will complete it by then. Sorry for any inconvenience and Thank you for your support. -QN Academy

Target Market(s)

Parents and students

Industry/Entity Type

Education

Requirements
Must have
• For online less fine print on the first page. The phone number and support text message. Back to School , Support Online learning KEV/NUR test prep should have some focus
Nice to have
• Discuss the platform We created a platform with live instructor interaction, virtual classroom, instructional videos, assessments, and practice to support every individual student’s need. We are confident in our ability to provide the most effective distance learning experience.
Should not have
• too much clunky and packed with content. Should be easy to read with color

```html
<!DOCTYPE html>
<html lang="en">
<head>
<meta charset="utf-8">
<title>QN Academy – Online Tutoring Flyer</title>
<link href="https://fonts.googleapis.com/css2?family=Open+Sans:wght@400;600;700&family=Roboto+Condensed:wght@400;700&family=Roboto+Slab:wght@300;400&display=swap" rel="stylesheet">
<style>
:root{
  --navy:#172a5e;
  --navy-deep:#0f1f4a;
  --navy-mid:#274a8c;
  --red:#c21f2e;
  --yellow:#f3c51b;
  --sky-light:#eef5fb;
  --sky:#b9d8ee;
  --cloud-blue:#7fd0f2;
  --ink:#3a3a3a;
  --page:#e9e7e4;
  --white:#ffffff;
}
*{box-sizing:border-box;margin:0;padding:0}
html,body{width:1200px;height:749px;overflow:hidden;background:var(--page)}
body{position:relative;font-family:"Open Sans",sans-serif}
.flyer{position:absolute;top:40px;width:520px;height:670px;overflow:hidden;background:var(--navy);box-shadow:0 2px 10px rgba(0,0,0,.25)}
.flyer--front{left:60px}
.flyer--back{left:620px}
.sky{position:absolute;left:0;top:0;width:100%;height:320px;background:linear-gradient(180deg,var(--sky) 0%,var(--sky-light) 55%,#dbe9f5 100%)}
.flyer--back .sky{height:240px;background:linear-gradient(160deg,#d6e8f6 0%,#f3f8fc 50%,#c3dcef 100%)}
.sky-curve{position:absolute;left:0;width:100%}
.navy-body{position:absolute;left:0;right:0;bottom:0;background:linear-gradient(180deg,var(--navy-mid) 0%,var(--navy) 45%,var(--navy-deep) 100%)}
.brand{position:absolute;left:26px;top:34px;display:flex;align-items:center;gap:10px}
.brand-square{width:30px;height:30px;background:var(--red)}
.brand-name{font-family:"Roboto Slab",serif;font-weight:400;font-size:20px;color:var(--navy);letter-spacing:.5px}
.headline{position:absolute;left:26px;font-family:"Roboto Slab",serif;font-weight:400;color:var(--red)}
.headline--main{top:108px;font-size:54px;line-height:54px;letter-spacing:1px}
.tagline{position:absolute;left:28px;top:214px;font-family:"Roboto Condensed",sans-serif;font-size:28px;line-height:32px;color:var(--navy);letter-spacing:.3px}
.cloud{position:absolute;left:24px;top:254px;width:222px;height:142px}
.cloud-text{position:absolute;left:24px;top:290px;width:222px;text-align:center;font-family:"Roboto Condensed",sans-serif;font-size:18px;line-height:22px;color:var(--white)}
.assess-title{position:absolute;left:28px;top:404px;width:230px;font-weight:700;line-height:17px;color:var(--yellow);font-family:"Roboto Condensed",sans-serif;font-size:14.5px}
.assess-list{position:absolute;left:28px;top:451px;width:222px;list-style:none}
.assess-list li{position:relative;padding-left:13px;font-size:10px;line-height:14px;color:var(--white);margin-bottom:15px}
.assess-list li::before{content:"";position:absolute;left:0;top:4px;width:6px;height:6px;border-radius:50%;background:var(--yellow)}
.highlights{position:absolute;left:260px;top:306px;width:252px;height:310px;background:var(--white);border-radius:8px;box-shadow:0 2px 6px rgba(0,0,0,.3);z-index:2}
.highlights-head{height:34px;background:var(--red);border-radius:8px 8px 0 0;color:var(--white);font-family:"Roboto Condensed",sans-serif;font-weight:400;font-size:21px;line-height:34px;text-align:center}
.highlights-list{list-style:none;padding:12px 12px 0 16px}
.highlights-list li{position:relative;padding-left:17px;font-size:10px;line-height:11.5px;color:var(--ink);margin-bottom:10px}
.highlights-list svg{position:absolute;left:0;top:0;width:11px;height:11px}
.footer{position:absolute;left:0;right:0;bottom:0;height:74px;background:var(--yellow);z-index:1}
.footer::before{content:"";position:absolute;left:0;right:0;top:-6px;height:6px;background:linear-gradient(135deg,var(--yellow) 50%,transparent 50%) 0 0/8px 6px repeat-x,linear-gradient(225deg,var(--yellow) 50%,transparent 50%) 0 0/8px 6px repeat-x}
.social{position:absolute;left:20px;top:12px;display:flex;gap:9px}
.social span{width:22px;height:22px;border-radius:50%;background:var(--red)}
.address{position:absolute;left:18px;top:44px;font-size:9.6px;line-height:13px;color:var(--navy);font-weight:600}
.address b{font-weight:700}
.phone{position:absolute;top:40px;left:302px;display:flex;align-items:center;gap:8px;font-weight:700;font-size:21px;line-height:24px;color:var(--red)}
.phone svg{width:22px;height:22px}
.hurry{position:absolute;right:24px;top:12px;font-family:"Roboto Condensed",sans-serif;font-size:17px;color:var(--navy)}
.back-headline{position:absolute;left:26px;top:80px;font-family:"Roboto Slab",serif;font-weight:300;font-size:25px;line-height:28px;color:var(--red)}
.photo{position:absolute;top:176px;width:156px;height:106px;border:2px solid var(--white);border-radius:6px;z-index:2}
.photo--writing{left:21px;background:linear-gradient(135deg,#f1e4dc,#c99c83)}
.photo--study{left:183px;background:linear-gradient(135deg,#e7ecef,#9fb0bd)}
.photo--laptop{left:344px;background:linear-gradient(135deg,#ece6e1,#b7a192)}
.subject{position:absolute;width:220px}
.subject-pill{display:inline-flex;align-items:center;gap:6px;height:18px;min-width:125px;padding:0 10px 0 8px;background:var(--yellow);border-radius:9px;color:var(--white);font-weight:700;font-family:"Roboto Condensed",sans-serif;font-size:13px;white-space:nowrap}
.subject-pill svg{width:12px;height:12px;flex:none}
.subject p{margin-top:4px;font-size:9.6px;line-height:10.6px;color:var(--white);text-align:justify;letter-spacing:-.15px}
.col-a{left:22px}.col-b{left:273px}
.row-1{top:298px}.row-2{top:398px}.row-3{top:498px}
</style>
</head>
<body>

<section class="flyer flyer--front">
  <div class="sky" role="img" aria-label="Photo of a child in a red cape and goggles riding a rocket through a bright cloudy sky"></div>
  <div class="navy-body" style="top:330px"></div>
  <svg class="sky-curve" style="top:280px" width="520" height="60" viewBox="0 0 520 60">
    <path d="M0 20 Q260 70 520 28 L520 60 L0 60 Z" fill="#274a8c"/>
    <path d="M0 20 Q260 70 520 28" fill="none" stroke="#f3c51b" stroke-width="2"/>
  </svg>

  <div class="brand"><span class="brand-square"></span><span class="brand-name">QN ACADEMY</span></div>
  <h1 class="headline headline--main">ONLINE<br>TUTORING</h1>
  <p class="tagline">STAY HOME STAY SAFE</p>

  <svg class="cloud" viewBox="0 0 240 150">
    <g fill="#ffffff">
      <circle cx="185" cy="22" r="18"/><circle cx="60" cy="62" r="42"/><circle cx="120" cy="52" r="46"/>
      <circle cx="180" cy="66" r="42"/><circle cx="55" cy="100" r="38"/><circle cx="120" cy="108" r="40"/><circle cx="185" cy="100" r="38"/>
    </g>
    <g fill="#7fd0f2">
      <circle cx="185" cy="22" r="15"/><circle cx="60" cy="62" r="39"/><circle cx="120" cy="52" r="43"/>
      <circle cx="180" cy="66" r="39"/><circle cx="55" cy="100" r="35"/><circle cx="120" cy="108" r="37"/><circle cx="185" cy="100" r="35"/>
    </g>
  </svg>
  <p class="cloud-text">DIGITAL LEARNING<br>FOR STUDENS<br>COVID-19 LOCKDOWN</p>

  <h2 class="assess-title">Comprehensive students assessment program spanning grades 3-12</h2>
  <ul class="assess-list">
    <li>Grade 3 through 8 take an end-of-grade assessment in Language Arts and Mathematics</li>
    <li>Grade 5 and 8 are also assessed in Science and Social Studies</li>
    <li>High school students take an end-of-course assessment (EOC)</li>
  </ul>

  <div class="highlights">
    <h2 class="highlights-head">COURSE HIGHLIGHTS</h2>
    <ul class="highlights-list">
      <li><svg viewBox="0 0 12 12"><circle cx="6" cy="6" r="5" fill="none" stroke="#c21f2e" stroke-width="1.3"/><path d="M5 3.5 7.5 6 5 8.5" fill="none" stroke="#c21f2e" stroke-width="1.3"/></svg>Two hours coaching (Language &amp; Math) every weekend</li>
      <li><svg viewBox="0 0 12 12"><circle cx="6" cy="6" r="5" fill="none" stroke="#c21f2e" stroke-width="1.3"/><path d="M5 3.5 7.5 6 5 8.5" fill="none" stroke="#c21f2e" stroke-width="1.3"/></svg>Additional one-hour coaching in Science and Social Studies (Grade 5 and 8 only)</li>
      <li><svg viewBox="0 0 12 12"><circle cx="6" cy="6" r="5" fill="none" stroke="#c21f2e" stroke-width="1.3"/><path d="M5 3.5 7.5 6 5 8.5" fill="none" stroke="#c21f2e" stroke-width="1.3"/></svg>Course begins in January and ends in April</li>
      <li><svg viewBox="0 0 12 12"><circle cx="6" cy="6" r="5" fill="none" stroke="#c21f2e" stroke-width="1.3"/><path d="M5 3.5 7.5 6 5 8.5" fill="none" stroke="#c21f2e" stroke-width="1.3"/></svg>Classes conducted by certified and experienced school teachers</li>
      <li><svg viewBox="0 0 12 12"><circle cx="6" cy="6" r="5" fill="none" stroke="#c21f2e" stroke-width="1.3"/><path d="M5 3.5 7.5 6 5 8.5" fill="none" stroke="#c21f2e" stroke-width="1.3"/></svg>Pre and post assessment to identify and resolve skill gaps</li>
      <li><svg viewBox="0 0 12 12"><circle cx="6" cy="6" r="5" fill="none" stroke="#c21f2e" stroke-width="1.3"/><path d="M5 3.5 7.5 6 5 8.5" fill="none" stroke="#c21f2e" stroke-width="1.3"/></svg>Online practice and skill checkpoints</li>
      <li><svg viewBox="0 0 12 12"><circle cx="6" cy="6" r="5" fill="none" stroke="#c21f2e" stroke-width="1.3"/><path d="M5 3.5 7.5 6 5 8.5" fill="none" stroke="#c21f2e" stroke-width="1.3"/></svg>Revise and practice full year syllabus to boost student confidence</li>
      <li><svg viewBox="0 0 12 12"><circle cx="6" cy="6" r="5" fill="none" stroke="#c21f2e" stroke-width="1.3"/><path d="M5 3.5 7.5 6 5 8.5" fill="none" stroke="#c21f2e" stroke-width="1.3"/></svg>Use industry-proven test preparation materials</li>
    </ul>
  </div>

  <footer class="footer">
    <div class="social"><span></span><span></span></div>
    <p class="address">2150 Oakmont Ridge Rd, Suite 210 Duluth, GA 30096<br><b>www.qnacademyga.com</b></p>
    <p class="phone"><svg viewBox="0 0 24 24"><circle cx="12" cy="12" r="10.5" fill="none" stroke="#c21f2e" stroke-width="2"/><path d="M8.5 7c.6-.5 1.3-.4 1.6.2l.9 1.8c.2.5.1 1-.3 1.3l-.6.5c.6 1.3 1.6 2.3 2.9 2.9l.5-.6c.3-.4.8-.5 1.3-.3l1.8.9c.6.3.7 1 .2 1.6l-.8.8c-.6.6-1.6.7-2.4.3-2.6-1.2-4.5-3.1-5.7-5.7-.4-.8-.3-1.8.3-2.4z" fill="#c21f2e"/></svg>404-555-0147</p>
  </footer>
</section>

<section class="flyer flyer--back">
  <div class="sky" role="img" aria-label="Photo of a smiling girl with a backpack and glasses leaping with arms outstretched against a light sky"></div>
  <div class="navy-body" style="top:225px"></div>
  <svg class="sky-curve" style="top:160px" width="520" height="70" viewBox="0 0 520 70">
    <path d="M0 22 Q220 80 520 40 L520 70 L0 70 Z" fill="#274a8c"/>
    <path d="M0 22 Q220 80 520 40" fill="none" stroke="#f3c51b" stroke-width="2"/>
  </svg>

  <div class="brand"><span class="brand-square"></span><span class="brand-name">QN ACADEMY</span></div>
  <h1 class="back-headline">DIGITAL LEARNING<br>FOR STUDENS<br>COVID-19 LOCKDOWN</h1>

  <div class="photo photo--writing" role="img" aria-label="Photo of a young girl writing in a notebook"></div>
  <div class="photo photo--study" role="img" aria-label="Photo of a boy studying at a desk"></div>
  <div class="photo photo--laptop" role="img" aria-label="Photo of a teenage student taking notes beside a computer"></div>

  <div class="subject col-a row-1">
    <h3 class="subject-pill"><svg viewBox="0 0 12 12"><circle cx="6" cy="6" r="5" fill="none" stroke="#fff" stroke-width="1.3"/><path d="M3.5 6.2 5.3 8 8.6 4.3" fill="none" stroke="#fff" stroke-width="1.3"/></svg>Writing</h3>
    <p>Our writing program helps students organize and articulate their own ideas to become confident, competent writers and thinkers. Students will learn different types of writing such as: Analytical, Persuasive, Narrative, Informative and Scientific.</p>
  </div>
  <div class="subject col-b row-1">
    <h3 class="subject-pill"><svg viewBox="0 0 12 12"><circle cx="6" cy="6" r="5" fill="none" stroke="#fff" stroke-width="1.3"/><path d="M3.5 6.2 5.3 8 8.6 4.3" fill="none" stroke="#fff" stroke-width="1.3"/></svg>Homework Help</h3>
    <p>Many students require help to understand a new concept, to solve a challenging problem, or complete an assignment. We help students overcome their problems and lead them to uncover and discover the right answers. Help is available after school hours and weekends.</p>
  </div>
  <div class="subject col-a row-2">
    <h3 class="subject-pill"><svg viewBox="0 0 12 12"><circle cx="6" cy="6" r="5" fill="none" stroke="#fff" stroke-width="1.3"/><path d="M3.5 6.2 5.3 8 8.6 4.3" fill="none" stroke="#fff" stroke-width="1.3"/></svg>Reading</h3>
    <p>We build strong reading comprehension skills with the right balance of informational and literacy texts from a wide range of genres; promote comprehension skills in emergent readers; and provide rigorous instruction on every reading standard in a developmentally appropriate way.</p>
  </div>
  <div class="subject col-b row-2">
    <h3 class="subject-pill"><svg viewBox="0 0 12 12"><circle cx="6" cy="6" r="5" fill="none" stroke="#fff" stroke-width="1.3"/><path d="M3.5 6.2 5.3 8 8.6 4.3" fill="none" stroke="#fff" stroke-width="1.3"/></svg>Computer Programming</h3>
    <p>This class exposes students to computer science at early ages to improve their understanding of technology. Programming is the new math; it stimulates thinking and enhance anylytical problem solving skills.</p>
  </div>
  <div class="subject col-a row-3">
    <h3 class="subject-pill"><svg viewBox="0 0 12 12"><circle cx="6" cy="6" r="5" fill="none" stroke="#fff" stroke-width="1.3"/><path d="M3.5 6.2 5.3 8 8.6 4.3" fill="none" stroke="#fff" stroke-width="1.3"/></svg>Math</h3>
    <p>Help young learners build the conceptual understanding needed to tackle more complex mathematical challenges. Develop mathematical reasoning through lessons that use real-world problem solving as instruction.</p>
  </div>
  <div class="subject col-b row-3">
    <h3 class="subject-pill"><svg viewBox="0 0 12 12"><circle cx="6" cy="6" r="5" fill="none" stroke="#fff" stroke-width="1.3"/><path d="M3.5 6.2 5.3 8 8.6 4.3" fill="none" stroke="#fff" stroke-width="1.3"/></svg>Critical Thinking</h3>
    <p>Our critical thinking courses are specially designed to make kids use in-depth analysis of evidence to make decisions and communicate their ideas clearly and accurately.</p>
  </div>

  <footer class="footer">
    <div class="social"><span></span><span></span></div>
    <p class="address">2150 Oakmont Ridge Rd, Suite 210 Duluth, GA 30096<br><b>www.qnacademyga.com</b></p>
    <p class="hurry">HURRY, LIMITED SPACE AVAILABLE</p>
    <p class="phone"><svg viewBox="0 0 24 24"><circle cx="12" cy="12" r="10.5" fill="none" stroke="#c21f2e" stroke-width="2"/><path d="M8.5 7c.6-.5 1.3-.4 1.6.2l.9 1.8c.2.5.1 1-.3 1.3l-.6.5c.6 1.3 1.6 2.3 2.9 2.9l.5-.6c.3-.4.8-.5 1.3-.3l1.8.9c.6.3.7 1 .2 1.6l-.8.8c-.6.6-1.6.7-2.4.3-2.6-1.2-4.5-3.1-5.7-5.7-.4-.8-.3-1.8.3-2.4z" fill="#c21f2e"/></svg>404-555-0147</p>
  </footer>
</section>

</body>
</html>
```